FREE DENTURES

The card will be placed on plastic stand at doctors office and Seniors centers. This is to acheive specific market segment of people that must have Evergard A & B card and FULL helpnet.
The size of the card shuold be 3.1/2" X 6" printed on vertical format. The basic design must have a picture of a denture and a eye glass frame.The content should be:
NEED DENTURES and/or EYE GLASSES?
NO COST TO YOU
Must have EVERGARD A & B and FULL HELPNET
Must qualify for program
No obligation Call today
BRAM OKUDA 555-238-0194
(Not affiliated with Norvale Union Authority, the Federal Evergard or the State Helpnet Program

Add at a proper side or top. 2 stripes, 1 Red, 1 blue in a waive format.

```html
<!DOCTYPE html>
<html lang="en">
<head>
<meta charset="utf-8">
<title>Need Dentures and or Eye Glasses?</title>
<link rel="stylesheet" href="https://fonts.googleapis.com/css2?family=Archivo+Black&family=Bitter:wght@700&family=Arimo:wght@400&display=swap">
<style>
  :root {
    --brand-blue: #0b4f9c;
    --brand-red: #e1232b;
    --paper: #ffffff;
    --photo-green: #4f7a3a;
    --photo-warm: #b98a6a;
  }
  * { margin: 0; padding: 0; box-sizing: border-box; }
  html, body { width: 674px; height: 1200px; overflow: hidden; background: var(--paper); }
  .card { position: relative; width: 674px; height: 1200px; background: var(--paper); overflow: hidden; }

  .headline {
    position: absolute; top: 22px; left: 0; width: 100%; text-align: center;
    font-family: "Archivo Black", "Arial Black", sans-serif; color: var(--brand-blue);
    font-size: 60px; line-height: 1; letter-spacing: 1px;
  }
  .subhead {
    position: absolute; top: 88px; left: 0; width: 100%; text-align: center;
    font-family: "Archivo Black", "Arial Black", sans-serif; color: var(--brand-blue);
    font-size: 28px; line-height: 1;
  }
  .hero { position: absolute; top: 130px; left: 0; width: 674px; height: 500px; }

  .requirements {
    position: absolute; top: 622px; left: 0; width: 100%; text-align: center;
    font-family: "Bitter", Georgia, serif; font-weight: 700; line-height: 1.18;
  }
  .requirements .blue { color: var(--brand-blue); font-size: 35px; }
  .requirements .red { color: var(--brand-red); font-size: 36px; letter-spacing: 0.5px; }

  .cta {
    position: absolute; top: 868px; left: 0; width: 100%; text-align: center;
    font-family: "Archivo Black", "Arial Black", sans-serif; color: var(--brand-blue);
    font-size: 30px; letter-spacing: 0.5px;
  }
  .contact {
    position: absolute; top: 910px; left: 0; width: 100%; text-align: center;
    font-family: "Archivo Black", "Arial Black", sans-serif; color: var(--brand-red);
    white-space: nowrap;
  }
  .contact .name { font-size: 30px; }
  .contact .phone { font-size: 42px; margin-left: 8px; }

  .offer-band {
    position: absolute; top: 990px; left: 0; width: 100%; height: 86px;
    background: var(--brand-red); color: var(--paper);
    font-family: "Archivo Black", "Arial Black", sans-serif; font-size: 54px;
    display: flex; align-items: center; justify-content: center;
  }
  .disclaimer-band {
    position: absolute; top: 1090px; left: 0; width: 100%; height: 50px;
    background: var(--brand-blue); color: var(--paper);
    font-family: "Arimo", Arial, sans-serif; font-size: 15.5px;
    display: flex; align-items: center; justify-content: center;
  }
  .footer-band { position: absolute; top: 1150px; left: 0; width: 100%; height: 50px; background: var(--brand-red); }
</style>
</head>
<body>
<div class="card">
  <h1 class="headline">NEED DENTURES</h1>
  <p class="subhead">AND OR EYE GLASSES?</p>

  <svg class="hero" viewBox="0 0 674 500" xmlns="http://www.w3.org/2000/svg">
    <defs>
      <linearGradient id="photoTone" x1="0" y1="0" x2="0" y2="1">
        <stop offset="0" stop-color="var(--photo-green)"/>
        <stop offset="0.45" stop-color="var(--photo-warm)"/>
        <stop offset="1" stop-color="#6d87b8"/>
      </linearGradient>
    </defs>
    <path role="img" aria-label="Group photo of smiling seniors outdoors" d="M0 0 H674 V335 Q337 605 0 335 Z" fill="url(#photoTone)"/>
    <path d="M0 335 Q337 605 674 335 V347 Q337 620 0 347 Z" fill="var(--brand-blue)"/>
    <path d="M0 347 Q337 620 674 347 V364 Q337 640 0 364 Z" fill="var(--brand-red)"/>
  </svg>

  <div class="requirements">
    <p class="blue">Must have:</p>
    <p class="red">EVERGARD A &amp; B</p>
    <p class="blue">and</p>
    <p class="red">FULL HELPNET</p>
    <p class="blue">Must qualify for program</p>
  </div>

  <p class="cta">No obligation Call today!</p>
  <p class="contact"><span class="name">Bram Okuda</span><span class="phone">555-238-0194</span></p>

  <div class="offer-band">NO COST TO YOU!!!</div>
  <div class="disclaimer-band">(Not affiliated with Norvale Union Authority, the Federal Evergard or the State Helpnet Program)</div>
  <div class="footer-band"></div>
</div>
</body>
</html>
```